Tito - Idiomas Corvalo

2x Design Concepts for the home page and interior pages based on the attached brief and powerpoint presentation.

Colours: see 2.1 logo and heading for logo colours and website colours

Home Page: (please see attached file)
1)Logo to appear in the top left, heading to include telephone numbers and a best price (credibility stamp) - see 2.1
2)the toolbar is to be centered at the top. Emphasis must be placed on the 5 easy steps to study english in Australia - see 2.2
3) modules. 5x modules required in the home page for: home page image rotator, online quote tool, enquiry form, best deals, quick links (there are 2 examples for the quick links module - open to suggestions) - see 2.3
4) footer. the footer is to include partner logos with hyperlinks to the partner websites. with a copywright section at the base - see 2.4
5) 2.5 is the basic idea - open to design suggestions. The website objective is to submit an online quote or contact Idiomas Corvalo.

Internal Page: - see 3-
open to all suggestion. Require a lot of space for internal custom design concepts (these are taking place inhouse). The interior page must have a side module toolbar to include:
1) a modified online quote tool
2) modified enquiry form
3) modified quick links section

Target Market(s)

target market is young (17-30yrs) Brazilians looking to study English in Australia or continue studying English in Australia that can also acquire visa sponsorship.

The buyer will be the parents of the students. the design must appeal to both markets.

Number of Pages Required

2 pages

Requirements
Must have
• see project overview
2x design concepts for the home page and interior page
professional, clean, simple and easy to navigate

```html
<!DOCTYPE html>
<html lang="pt-BR">
<head>
<meta charset="utf-8">
<title>Idiomas Corvalo – Estude inglês na Austrália</title>
<link rel="stylesheet" href="https://fonts.googleapis.com/css2?family=Arimo:wght@400;700&display=swap">
<style>
:root{
  --navy:#2d5080;
  --navy-dark:#23436d;
  --green-top:#7fb04a;
  --green-bot:#4f8a2a;
  --panel:#e8e2bd;
  --panel-line:#8d8a6c;
  --ink:#1a1a1a;
  --logo-green:#2f6b3a;
  --gold:#d7a63a;
  --link-blue:#2b4f9a;
  --white:#ffffff;
}
*{box-sizing:border-box;margin:0;padding:0}
html,body{width:900px;height:1200px;overflow:hidden;background:var(--white)}
body{position:relative;font-family:"Arimo",Arial,sans-serif;color:var(--ink)}
.abs{position:absolute}

/* header */
.brand{left:20px;top:28px;font-size:27px;font-weight:700;color:var(--logo-green);letter-spacing:.5px}
.brand-sub{left:150px;top:60px;font-size:15px;font-weight:700;color:var(--logo-green)}
.badge{left:584px;top:20px;width:62px;height:62px;border-radius:50%;background:radial-gradient(circle at 40% 35%,#f0cb6a,var(--gold) 70%,#b08224)}
.flag{width:44px;height:40px;border-radius:8px}
.flag-au{left:718px;top:2px;background:linear-gradient(135deg,#1f3f8f,#2c56b8)}
.flag-br{left:714px;top:48px;background:linear-gradient(135deg,#2f9a3a,#f0d23a 55%,#2f9a3a)}
.phone{left:782px;font-size:15px;color:#4a4a4a;letter-spacing:1px}

/* nav */
.nav{left:0;top:108px;width:900px;height:57px;background:var(--navy);display:flex;align-items:center;justify-content:space-around;padding:0 10px}
.nav a{color:var(--white);text-decoration:none;font-size:15px;display:flex;align-items:center;gap:6px}

/* hero */
.hero{left:0;top:165px;width:900px;height:292px;background:linear-gradient(90deg,#9fb89a 0%,#e8eee6 35%,#f4f6f4 70%,#d9c6a0 100%)}
.dots{right:8px;top:437px;display:flex;gap:3px}
.dots span{width:18px;height:18px;background:var(--navy-dark);color:var(--white);font-size:11px;font-weight:700;display:flex;align-items:center;justify-content:center}

/* steps */
.steps{left:0;top:457px;width:900px;height:86px;background:var(--navy);display:flex;justify-content:space-between;padding:15px 6px 0}
.step{width:170px;height:52px;border-radius:5px;background:linear-gradient(var(--green-top),var(--green-bot));border:1px solid #3c6d20;color:var(--white);font-size:16px;display:flex;align-items:center;justify-content:center;text-align:center;line-height:1.2}

/* panels */
.panel{background:var(--panel);border:1px solid var(--panel-line);border-radius:8px}
.panel::before{content:"";position:absolute;left:8px;top:-1px;width:90px;height:2px;background:#111}
.panel-title{text-align:center;font-size:13px;padding-top:14px}
.enquire{left:25px;top:545px;width:260px;height:290px}
.deals{left:296px;top:545px;width:322px;height:290px}
.quote{left:629px;top:545px;width:264px;height:290px}
.quicklinks{left:25px;top:844px;width:591px;height:187px}
.partners{left:627px;top:844px;width:266px;height:187px}

.intro{left:13px;top:42px;width:236px;font-size:11px;line-height:1.35}
.field-label{left:14px;font-size:12px}
.field{left:88px;width:147px;height:19px;background:var(--white);border:1px solid #a9a690;font-size:9px;padding:3px 10px}
.btn{height:20px;background:linear-gradient(#fff,#e4e0cf);border:1px solid #9a9788;border-radius:4px;font-size:10px;color:#333;display:flex;align-items:center;gap:6px;padding:0 8px}
.btn::before{content:"";border-left:4px solid transparent;border-right:4px solid transparent;border-bottom:6px solid #c0302a}

.deal-row{left:19px;width:286px;font-size:12px;display:flex;justify-content:space-between;letter-spacing:.3px}
.more{right:16px;left:auto;width:auto;font-size:11px}

.states{left:8px;top:80px;font-size:12px;line-height:21px;letter-spacing:.3px}
.states div{display:flex;align-items:center;gap:9px}
.radio{width:12px;height:12px;border:1px solid #444;border-radius:50%;background:var(--white);position:relative}
.radio.on::after{content:"";position:absolute;left:3px;top:3px;width:4px;height:4px;border-radius:50%;background:#111}
.select{left:119px;top:78px;width:128px;height:21px;background:linear-gradient(#fff,#dcdcdc);border:1px solid #888;font-size:11px;letter-spacing:1.5px;display:flex;align-items:center;justify-content:center}
.cards{left:24px;top:244px;display:flex;gap:12px}
.card{font-size:9px;font-weight:700;color:#333;display:flex;align-items:center;gap:4px}
.card i{width:10px;height:10px;background:#7b7b7b;display:block}

.tile{width:150px;height:48px;display:flex;gap:8px;font-size:8.5px;line-height:1.35}
.tile.boxed{background:var(--white);border-radius:6px;padding:4px}
.tile-icon{width:40px;height:40px;border-radius:50%;flex:none;background:radial-gradient(circle at 40% 35%,#4aa0e0,#1f5fa8)}
.tile-icon.kids{background:radial-gradient(circle,#f4f0e6,#d8cdb8);border:1px solid #c33}
.tile b{font-weight:400;font-size:8px;display:block}

.partner-name{font-size:14px;font-weight:700;color:#4a4a4a;display:flex;align-items:center;gap:6px}
.partner-name i{width:12px;height:12px;background:#8a8a8a;display:block}

/* footer */
.footer-col{top:1048px;font-size:9.5px;line-height:17.5px;color:#333;letter-spacing:.3px}
.footer-col h4{font-size:9.5px;color:var(--link-blue)}
.copyright{left:150px;top:1158px;width:680px;font-size:8.5px;color:var(--link-blue);line-height:1.35}
.copyright b{font-size:9px}
</style>
</head>
<body>

<header>
  <div class="abs brand">IDIOMASCORVALO</div>
  <div class="abs brand-sub">.com.br</div>
  <div class="abs badge" role="img" aria-label="Selo de melhor preço"></div>
  <div class="abs flag flag-au" role="img" aria-label="Bandeira da Austrália"></div>
  <div class="abs phone" style="top:12px">0 800 555 010</div>
  <div class="abs flag flag-br" role="img" aria-label="Bandeira do Brasil"></div>
  <div class="abs phone" style="top:65px">1 800 555 020</div>
</header>

<nav class="abs nav">
  <a>Home</a><a>Promotions</a><a>Cities <span>›</span></a><a>Schools <span>›</span></a><a>Air Tickets</a><a>Visa</a><a>Final Details</a><a>Contact</a><a>Blog</a>
</nav>

<div class="abs hero" role="img" aria-label="Foto de três estudantes sorridentes em frente a computadores, com pilha de livros coloridos e mouse"></div>
<div class="abs dots"><span>1</span><span>2</span><span>3</span><span>4</span></div>

<div class="abs steps">
  <div class="step">Cidades</div>
  <div class="step">Escolas</div>
  <div class="step">Passagem<br>Aerea</div>
  <div class="step">Visto</div>
  <div class="step">Detalhes<br>Finais</div>
</div>

<section class="abs panel enquire">
  <div class="panel-title">Enquire Form</div>
  <p class="abs intro">Lorem ipsum dotor site amer consuterere adfc send diarm normmy mbh touchart</p>
  <div class="abs field-label" style="top:93px">Name:</div>
  <div class="abs field" style="top:91px">your user's name</div>
  <div class="abs field-label" style="top:120px">E-mail:</div>
  <div class="abs field" style="top:118px">E-mail ID</div>
  <div class="abs field-label" style="top:147px">Telephone:</div>
  <div class="abs field" style="top:145px">Telephone Number</div>
  <div class="abs field-label" style="top:175px">Messages:</div>
  <div class="abs field" style="top:172px;height:55px">Message</div>
  <div class="abs btn" style="left:142px;top:247px;width:90px">submit form</div>
</section>

<section class="abs panel deals">
  <div class="panel-title">Best Deals</div>
  <div class="abs deal-row" style="top:73px">IN AUSTRALIA</div>
  <div class="abs deal-row" style="top:113px"><span>Brisbane</span><span>from&nbsp;&nbsp;$89*</span></div>
  <div class="abs deal-row" style="top:147px"><span>Baliina Byron Bay</span><span>from&nbsp;&nbsp;$79*</span></div>
  <div class="abs deal-row" style="top:180px"><span>Gold Cost</span><span>from&nbsp;&nbsp;$85*</span></div>
  <div class="abs deal-row" style="top:213px"><span>Hamilton Island</span><span>from&nbsp;&nbsp;$65*</span></div>
  <div class="abs deal-row more" style="top:263px">More Domestic Flights&nbsp;›</div>
</section>

<section class="abs panel quote">
  <div class="panel-title">Online quote</div>
  <div class="abs" style="left:13px;top:44px;font-size:14px">States:</div>
  <div class="abs" style="left:152px;top:57px;font-size:11px">DURACAO</div>
  <div class="abs states">
    <div><span class="radio on"></span>Sydney</div>
    <div><span class="radio"></span>Melbourne</div>
    <div><span class="radio"></span>Gold Coast</div>
    <div><span class="radio"></span>Perth</div>
    <div><span class="radio"></span>Adelaide</div>
    <div><span class="radio"></span>Byron Bay</div>
  </div>
  <div class="abs select">Semister&nbsp;&nbsp;⇕</div>
  <div class="abs btn" style="left:157px;top:118px;width:90px">submit form</div>
  <div class="abs cards">
    <span class="card"><i></i>Carta</span>
    <span class="card"><i></i>Orbe</span>
    <span class="card"><i></i>Centauro</span>
    <span class="card"><i></i>Mesa</span>
  </div>
</section>

<section class="abs panel quicklinks">
  <div class="abs tile" style="left:8px;top:18px"><span class="tile-icon" role="img" aria-label="Ícone de atividades"></span><div><b>Activities</b>Help improve the l ives of some of the worls poorest choder</div></div>
  <div class="abs tile boxed" style="left:210px;top:18px;width:178px"><span class="tile-icon kids" role="img" aria-label="Ícone infantil"></span><div><b>SunKids</b>Help improve the l ives of some of the worls poorest choder</div></div>
  <div class="abs tile" style="left:398px;top:18px"><span class="tile-icon" role="img" aria-label="Ícone de atividades"></span><div><b>Activities</b>Help improve the l ives of some of the worls poorest choder</div></div>
  <div class="abs tile boxed" style="left:8px;top:105px;width:178px"><span class="tile-icon kids" role="img" aria-label="Ícone infantil"></span><div><b>SunKids</b>Help improve the l ives of some of the worls poorest choder</div></div>
  <div class="abs tile" style="left:204px;top:105px"><span class="tile-icon" role="img" aria-label="Ícone de atividades"></span><div><b>Activities</b>Help improve the l ives of some of the worls poorest choder</div></div>
  <div class="abs tile boxed" style="left:400px;top:105px;width:178px"><span class="tile-icon kids" role="img" aria-label="Ícone infantil"></span><div><b>SunKids</b>Help improve the l ives of some of the worls poorest choder</div></div>
</section>

<section class="abs panel partners">
  <div class="panel-title" style="text-decoration:underline">Partners Logos</div>
  <div class="abs partner-name" style="left:70px;top:60px"><i></i>PagoVia</div>
  <div class="abs partner-name" style="left:76px;top:88px"><i></i>RedeIdeia</div>
  <div class="abs partner-name" style="left:70px;top:118px"><i></i>Cobrafix</div>
</section>

<footer>
  <div class="abs footer-col" style="left:279px"><h4>PagoVia</h4>Quem somos<br>Parceiros<br>Na mídia<br>Mapa do site</div>
  <div class="abs footer-col" style="left:388px"><h4>Serviços</h4>Para vendedores<br>Para compradores<br>Tarifas</div>
  <div class="abs footer-col" style="left:521px"><h4>Usuário</h4>Login<br>Cadastro<br>Termos de uso<br>Segurança para vendedores<br>Segurança para compradores</div>
  <p class="abs copyright"><b>PagoVia | Copyright © 2007-2008. Todos os direitos reservados.</b><br>PagoVia é um serviço da PagoVia Pagamentos S.A., empresa prestadora de serviços de gestão de pagamentos na internet, que atua como agente por conta e ordem dos usuários. O serviço não é, e nem se destina, a ser comparável a serviços financeiros. O uso deste site implica na aceitação dos nossos termos.</p>
</footer>

</body>
</html>
```